I need professional letterhead for an attorney. I already have my logo (attached). I currently have a project going to get business cards. I would like the letterhead to be classy. It is very important that this letterhead be in a format that I can import it into Microsoft Word 2013. I plan on importing this into Word so I can type my documents directly onto it and electronically send the finished documents to my clients. Thank you very much.

Industry/Entity Type

Attorney

Requirements
Must have
• Here is my info. Please put it all on there:
• Dwight R. Mallory Attorney At Law
• 48613 Brackwell Crescent
• St. Louis, MO 63047
• Telephone: 314-596-2043
• Fax: 800-627-4915
• Email: Dwight@RivermarkWills.com
• Also, I need the ability to import this final design into Microsoft Word 2013 so that I can type directly onto it. I believe I can do that if you hand it over to me as a JPG and a PDF in addition to the other formats. Then I should be able to import it into Word.

```html
<!DOCTYPE html>
<html lang="en">
<head>
<meta charset="utf-8">
<title>Rivermark Wills LLC – Letterhead</title>
<link href="https://fonts.googleapis.com/css2?family=Tinos&family=Archivo+Narrow:wght@400&display=swap" rel="stylesheet">
<style>
  :root {
    --brand-blue: #1f7bc0;
    --ink: #111111;
    --paper: #ffffff;
    --mark-tint: #eaf1f7;
  }
  * { margin: 0; padding: 0; box-sizing: border-box; }
  html, body {
    width: 849px;
    height: 1200px;
    overflow: hidden;
    background: var(--paper);
  }
  .letterhead {
    position: relative;
    width: 849px;
    height: 1200px;
    background: var(--paper);
  }
  .brand {
    position: absolute;
    left: 54px;
    top: 76px;
    display: flex;
    align-items: center;
    gap: 10px;
  }
  .brand-dot {
    width: 54px;
    height: 54px;
    border-radius: 50%;
    background: var(--brand-blue);
    flex: none;
  }
  .brand-name {
    font-family: "Tinos", "Times New Roman", serif;
    font-size: 27px;
    letter-spacing: 0.5px;
    color: var(--brand-blue);
    white-space: nowrap;
  }
  .contact {
    position: absolute;
    top: 77px;
    font-family: "Archivo Narrow", "Arial Narrow", sans-serif;
    font-size: 12.5px;
    line-height: 15.6px;
    color: var(--ink);
    font-style: normal;
  }
  .contact-address { left: 469px; }
  .contact-lines { left: 656px; }
  .backdrop-mark {
    position: absolute;
    left: 300px;
    top: 893px;
  }
</style>
</head>
<body>
  <main class="letterhead">
    <header>
      <div class="brand">
        <span class="brand-dot"></span>
        <span class="brand-name">RIVERMARK WILLS LLC</span>
      </div>
      <address class="contact contact-address">
        Dwight R. Mallory Attorney At Law<br>
        48613 Brackwell Crescent<br>
        St. Louis, MO 63047
      </address>
      <address class="contact contact-lines">
        Telephone: 314-596-2043<br>
        Fax: 800-627-4915<br>
        Email: Dwight@RivermarkWills.com
      </address>
    </header>
    <svg class="backdrop-mark" width="254" height="254" viewBox="0 0 254 254" aria-hidden="true">
      <circle cx="127" cy="127" r="127" fill="var(--mark-tint)"/>
    </svg>
  </main>
</body>
</html>
```